Tour agency for FIT and groups need a business card design

We need a business card design for a tour agency company that is based in Perth called" BRISK NO", we aim to provide customise, unique and seamless travel arrangement for FIT and groups. We serve both high profile businessperson, government authorities, business partners, executives and investors. The name card should be more professional looking.
Updates

Project Deadline Extended Reason: Have some changes that needed to make, director will be back to office on Monday, sorry for the inconvenience cause. Added Saturday, May 6, 2017

Target Market(s)

High profile businessperson, government authorities, business partners, executives and investors.

Industry/Entity Type

Tourism

Contact Information for Business Card

Brisk NO
Level 1, 214 Marlowe Avenue, Dunreath NO, 6120
www.briskno.com.au

Font styles to use
Serif

Colors

Designer to choose colors to be used in the design.

Requirements
Must have
• My project must have a company logo
Nice to have
• a more professional and solid yet friendly name card design. We may want to include chinese name in the name card as well. Edge of the card can be filled with gold and we think that transparent name cards are interesting.

```html
<!DOCTYPE html>
<html lang="en">
<head>
<meta charset="utf-8">
<title>Brisk NO — Business Card</title>
<link href="https://fonts.googleapis.com/css2?family=Playfair+Display:wght@400;700&display=swap" rel="stylesheet">
<style>
  :root {
    --backdrop: #e7e5e2;
    --card-black: #0b0b0c;
    --card-charcoal: #2a2a2b;
    --card-white: #ffffff;
    --ink: #3a3839;
    --ink-soft: #6a6768;
    --band: #2f2c2d;
    --band-text: #d9d7d7;
    --logo-white: #ffffff;
  }
  * { margin: 0; padding: 0; box-sizing: border-box; }
  html, body {
    width: 1200px; height: 1200px; overflow: hidden;
    background: var(--backdrop);
    font-family: "Playfair Display", Georgia, serif;
  }
  .canvas {
    position: relative; width: 1200px; height: 1200px;
    display: flex; flex-direction: column; align-items: center; justify-content: center; gap: 70px;
  }
  .card {
    position: relative; width: 760px; height: 434px;
    box-shadow: 0 10px 28px rgba(0,0,0,0.18);
  }
  /* Front */
  .card-front {
    background: linear-gradient(160deg, var(--card-black) 0%, var(--card-black) 35%, var(--card-charcoal) 100%);
    display: flex; align-items: center; justify-content: center;
  }
  .brand {
    display: flex; align-items: center; gap: 18px;
    color: var(--logo-white);
  }
  .brand-dot {
    width: 46px; height: 46px; border-radius: 50%; background: var(--logo-white);
  }
  .brand-name {
    font-size: 44px; font-weight: 400; letter-spacing: 4px;
  }
  /* Back */
  .card-back { background: var(--card-white); }
  .identity {
    position: absolute; left: 150px; top: 120px;
    display: flex; align-items: stretch;
  }
  .person {
    text-align: right; padding-right: 18px; padding-top: 4px;
  }
  .person-name {
    font-size: 27px; font-weight: 700; color: var(--ink-soft); letter-spacing: 0.5px;
  }
  .person-role {
    font-size: 19px; font-style: italic; color: var(--ink-soft); margin-top: 2px;
  }
  .divider { width: 1px; background: var(--ink-soft); }
  .contacts {
    list-style: none; padding-left: 16px; padding-top: 4px;
    display: flex; flex-direction: column; gap: 6px;
  }
  .contact {
    display: flex; align-items: center; gap: 10px;
    font-size: 19px; font-style: italic; color: var(--ink);
  }
  .contact svg { width: 18px; height: 18px; flex: none; }
  .address-band {
    position: absolute; left: 0; right: 0; top: 322px; height: 46px;
    background: var(--band);
    display: flex; align-items: center; padding-left: 28px;
    color: var(--band-text); font-size: 20px; letter-spacing: 0.6px;
  }
</style>
</head>
<body>
<main class="canvas">
  <section class="card card-front" aria-label="Card front">
    <div class="brand">
      <span class="brand-dot"></span>
      <span class="brand-name">BRISK NO</span>
    </div>
  </section>

  <section class="card card-back" aria-label="Card back">
    <div class="identity">
      <div class="person">
        <p class="person-name">ALEX MERCER</p>
        <p class="person-role">Director</p>
      </div>
      <span class="divider"></span>
      <ul class="contacts">
        <li class="contact">
          <svg viewBox="0 0 18 18"><rect x="4" y="1" width="10" height="16" rx="2" fill="none" stroke="#3a3839" stroke-width="1.6"/><rect x="6" y="3.5" width="6" height="8" fill="#3a3839"/></svg>
          555-218-4470
        </li>
        <li class="contact">
          <svg viewBox="0 0 18 18"><circle cx="9" cy="9" r="7.5" fill="none" stroke="#3a3839" stroke-width="1.4"/><ellipse cx="9" cy="9" rx="3.5" ry="7.5" fill="none" stroke="#3a3839" stroke-width="1.2"/><line x1="1.5" y1="9" x2="16.5" y2="9" stroke="#3a3839" stroke-width="1.2"/></svg>
          www.briskno.com.au
        </li>
        <li class="contact">
          <svg viewBox="0 0 18 18"><rect x="1.5" y="4" width="15" height="10" fill="#3a3839"/><polyline points="1.5,4 9,10 16.5,4" fill="none" stroke="#ffffff" stroke-width="1.2"/></svg>
          alex@briskno.com.au
        </li>
      </ul>
    </div>
    <div class="address-band">Level 1, 214 Marlowe Avenue, Dunreath NO, 6120</div>
  </section>
</main>
</body>
</html>
```